Flyer for Merchant Capital Cash Advance business

Need Flyer Design to be advertised on Social Media Platforms and also Print it to Publish it in Magazines.
Flyer Will be printed in different sizes for different publications.
Size 1) 6.25 inches * 11 inches.
Size 2) 8 inch * 11 inch
Size 3) 8 inch * 5.5 I inch
Size 4) 5 inch * 7 inch.
Google “Merchant Capital Cash advance flyer pics” to get an idea.

Flyer Design for Merchant Cash advance business.

Merchant Cash Advance is alternate to bank loans and does not require Personal Guarantee or Collateral.
Updates

Need extra days to review

Target Market(s)

Business owners seeking loan.

Industry/Entity Type

Business Service

Font styles to use
Serif
Sans Serif
Decorative
Script

Colors

Designer to choose colors to be used in the design.

Requirements
Must have
• Content from the Files Uploaded.
• Sharp Colors.
Nice to have
• Would like to see flyer in shape of a Bank Check or a $100 Bill.
• Would like to show a Comparison between Bank Loan and MCA.
• Open to any other ideas.

```html
<!DOCTYPE html>
<html lang="en">
<head>
<meta charset="utf-8">
<title>Business Capital Cash Advance</title>
<link rel="stylesheet" href="https://fonts.googleapis.com/css2?family=Oswald:wght@500;700&family=Open+Sans:wght@400;600&display=swap">
<style>
  :root {
    --navy: #15415c;
    --yellow: #fdd000;
    --pale-yellow: #fbeeab;
    --pale-blue: #a9c4cf;
    --white: #ffffff;
    --photo-light: #b9b9b9;
    --photo-dark: #3a3a3a;
  }
  html, body {
    margin: 0;
    padding: 0;
    overflow: hidden;
    background: #ffffff;
  }
  .flyer {
    position: relative;
    width: 1200px;
    height: 508px;
    overflow: hidden;
    font-family: "Open Sans", Arial, sans-serif;
    color: var(--white);
  }
  .flyer-shapes {
    position: absolute;
    inset: 0;
  }
  .headline {
    position: absolute;
    left: 33px;
    top: 136px;
    margin: 0;
    font-family: "Oswald", "Arial Narrow", sans-serif;
    font-weight: 700;
    font-size: 62px;
    line-height: 80px;
    text-transform: uppercase;
    letter-spacing: 0.5px;
  }
  .headline span { display: block; }
  .headline .accent { color: var(--yellow); }
  .diamond-text {
    position: absolute;
    left: 400px;
    top: 163px;
    width: 200px;
    margin: 0;
    text-align: center;
    font-family: "Oswald", "Arial Narrow", sans-serif;
    font-weight: 500;
    font-size: 29px;
    line-height: 53px;
    letter-spacing: 1px;
    text-transform: uppercase;
  }
  .compare-title {
    position: absolute;
    left: 709px;
    top: 33px;
    margin: 0;
    font-family: "Oswald", "Arial Narrow", sans-serif;
    font-weight: 700;
    font-size: 33px;
    line-height: 56px;
    letter-spacing: 3px;
    text-transform: uppercase;
  }
  .compare-title span { display: block; }
  .compare-title .accent { color: var(--yellow); }
  .compare-head {
    position: absolute;
    top: 150px;
    width: 60px;
    text-align: center;
    font-family: "Oswald", "Arial Narrow", sans-serif;
    font-weight: 700;
    font-size: 15px;
    letter-spacing: 0.5px;
  }
  .compare-head.mca { left: 1021px; }
  .compare-head.loan { left: 1103px; }
  .benefit-list {
    position: absolute;
    left: 730px;
    top: 180px;
    margin: 0;
    padding: 0;
    list-style: none;
  }
  .benefit-list li {
    position: relative;
    height: 39px;
    padding-left: 17px;
    font-size: 19px;
    line-height: 26px;
  }
  .benefit-list li::before {
    content: "";
    position: absolute;
    left: 0;
    top: 11px;
    width: 5px;
    height: 5px;
    border-radius: 50%;
    background: var(--yellow);
  }
  .contact-fields {
    position: absolute;
    left: 0;
    top: 456px;
    width: 1200px;
    font-size: 19px;
    line-height: 26px;
  }
  .contact-fields span { position: absolute; top: 0; }
  .field-name { left: 552px; }
  .field-email { left: 801px; }
  .field-phone { left: 1022px; }
</style>
</head>
<body>
<main class="flyer">
  <svg class="flyer-shapes" width="1200" height="508" viewBox="0 0 1200 508">
    <defs>
      <linearGradient id="money-tone" x1="0" y1="0" x2="1" y2="1">
        <stop offset="0" stop-color="var(--photo-light)"/>
        <stop offset="0.55" stop-color="#7a7a7a"/>
        <stop offset="1" stop-color="var(--photo-dark)"/>
      </linearGradient>
    </defs>
    <rect class="money-photo" x="0" y="0" width="680" height="508" fill="url(#money-tone)" role="img" aria-label="Black and white photograph of stacked dollar bills"/>
    <polygon class="accent-square-blue" points="228,0 432,0 330,102" fill="var(--pale-blue)"/>
    <polygon class="accent-square-yellow" points="360,128 430,58 500,128 430,198" fill="var(--pale-yellow)"/>
    <polygon class="info-panel" points="412,0 1200,0 1200,508 398,508 655,243" fill="var(--navy)"/>
    <polyline class="panel-edge" points="412,0 655,243 398,508" fill="none" stroke="var(--yellow)" stroke-width="8"/>
    <polygon class="diamond-fill" points="365,243 500,108 635,243 500,378" fill="var(--yellow)" stroke="var(--white)" stroke-width="4"/>
    <g class="mark-plus" fill="var(--yellow)">
      <circle cx="1051" cy="196" r="9"/>
      <circle cx="1051" cy="235" r="9"/>
      <circle cx="1051" cy="274" r="9"/>
      <circle cx="1051" cy="313" r="9"/>
      <circle cx="1051" cy="352" r="9"/>
      <circle cx="1051" cy="391" r="9"/>
    </g>
    <g class="mark-plus-sign" stroke="var(--navy)" stroke-width="1.6">
      <path d="M1047 196h8M1051 192v8M1047 235h8M1051 231v8M1047 274h8M1051 270v8M1047 313h8M1051 309v8M1047 352h8M1051 348v8M1047 391h8M1051 387v8"/>
    </g>
    <g class="mark-minus" fill="var(--yellow)">
      <circle cx="1133" cy="196" r="9"/>
      <circle cx="1133" cy="235" r="9"/>
      <circle cx="1133" cy="274" r="9"/>
      <circle cx="1133" cy="313" r="9"/>
      <circle cx="1133" cy="352" r="9"/>
      <circle cx="1133" cy="391" r="9"/>
    </g>
    <g class="mark-minus-sign" stroke="var(--navy)" stroke-width="1.6">
      <path d="M1129 196h8M1129 235h8M1129 274h8M1129 313h8M1129 352h8M1129 391h8"/>
    </g>
    <line class="column-divider" x1="1093" y1="188" x2="1093" y2="400" stroke="var(--yellow)" stroke-width="2"/>
    <line class="form-rule" x1="482" y1="434" x2="1200" y2="434" stroke="var(--white)" stroke-opacity="0.7" stroke-width="1"/>
    <g class="field-divider" stroke="var(--yellow)" stroke-width="1.5">
      <line x1="687" y1="481" x2="703" y2="459"/>
      <line x1="933" y1="481" x2="949" y2="459"/>
    </g>
  </svg>

  <h1 class="headline">
    <span>Get</span>
    <span>Business</span>
    <span class="accent">Capital Cash</span>
    <span class="accent">Advance</span>
  </h1>

  <p class="diamond-text">Need<br>Business<br>Capital<br>?</p>

  <h2 class="compare-title">
    <span>A Convenient Alternative</span>
    <span class="accent">To Bank Loan</span>
  </h2>

  <div class="compare-head mca">MCA</div>
  <div class="compare-head loan">LOAN</div>

  <ul class="benefit-list">
    <li>No Personal Guarantee</li>
    <li>No Minimum Credit Score</li>
    <li>No Collaterals needed</li>
    <li>No Guarantors needed</li>
    <li>Bankruptcy - OK</li>
    <li>Simple One Page Application</li>
  </ul>

  <div class="contact-fields">
    <span class="field-name">Business Name</span>
    <span class="field-email">Email</span>
    <span class="field-phone">Phone number</span>
  </div>
</main>
</body>
</html>
```